Tidewell Homecare

I am looking to have a website designed for a housekeeping company that looks similar to this one. https://marlowsnestcare.example/

I need 5 websites designed but will start with this one to see how I like it.

Industry/Entity Type

House Cleaning

Coding

Coded - Design and coding required

Number of Pages Required

5+ page

Font styles to use
Serif
Script

Colors
ffffff
fdf9cf
fbf289
fbee3f
d6edf3
86cae7
33a6d7
edf1f8
cedeed

```html
<!DOCTYPE html>
<html lang="en">
<head>
<meta charset="utf-8">
<title>Tidewell Homecare</title>
<link href="https://fonts.googleapis.com/css2?family=Dancing+Script:wght@600;700&family=Poppins:wght@400;500;600;700&display=swap" rel="stylesheet">
<style>
:root{
  --navy:#1b2a8c;
  --navy-form:#22359d;
  --yellow:#fcc500;
  --teal:#37b5a3;
  --ink:#1d1d2b;
  --muted:#4b4b58;
  --sky:#33a6d7;
  --sky-light:#86cae7;
  --mist:#edf1f8;
  --white:#ffffff;
  --line:#e4e6ee;
}
*{box-sizing:border-box;margin:0;padding:0}
html,body{width:1200px;height:2656px;overflow:hidden}
body{position:relative;background:var(--white);font-family:'Poppins',sans-serif;color:var(--ink)}
.abs{position:absolute}
.script{font-family:'Dancing Script',cursive;font-weight:700}
.social{display:flex;gap:8px}
.social span{width:32px;height:32px;border-radius:50%;background:#eef0f5;display:block;position:relative}
.social span::after{content:"";position:absolute;left:13px;top:13px;width:6px;height:6px;border-radius:50%;background:var(--navy)}
/* top bar */
.topbar{left:0;top:0;width:1200px;height:60px;border-bottom:1px solid var(--line)}
.contact-item{display:flex;gap:12px;align-items:flex-start}
.contact-item small{display:block;font-size:10.5px;color:var(--muted)}
.contact-item b{font-size:11.5px;font-weight:400}
.contact-item .big{font-size:15px;font-weight:700}
/* nav */
.brand{display:flex;align-items:center;gap:10px}
.brand i{width:40px;height:40px;border-radius:50%;background:var(--sky);display:block}
.brand span{font-size:22px;font-weight:600;color:var(--sky)}
.nav{display:flex;gap:20px;font-size:11px;font-weight:500;letter-spacing:.2px}
.nav a{color:var(--ink);text-decoration:none}
.nav a.on{color:var(--navy)}
.btn{display:flex;align-items:center;justify-content:center;gap:14px;border-radius:20px;font-size:11px;font-weight:600;letter-spacing:.2px}
.btn-yellow{background:var(--yellow);color:var(--ink)}
.btn-navy{background:var(--navy);color:var(--white)}
/* hero */
.hero{left:0;top:157px;width:1200px;height:420px;background:linear-gradient(120deg,#8a7866 0%,#b5a48f 30%,#6f6355 55%,#9c8a74 80%,#5e6b86 100%)}
.hero-shade{left:0;top:0;width:100%;height:100%;background:rgba(20,20,30,.28)}
.hero h1{top:120px;width:100%;text-align:center;color:var(--white);font-size:35px}
.hero p{top:172px;left:340px;width:520px;text-align:center;color:var(--white);font-size:12.5px;line-height:16.5px}
/* cards */
.card{top:630px;width:366px;height:250px;text-align:center}
.card h2{position:absolute;top:83px;width:100%;font-size:24px}
.card p{position:absolute;top:122px;left:38px;width:290px;font-size:9.5px;line-height:15px}
.card .btn{position:absolute;top:186px;left:78px;width:211px;height:36px;justify-content:space-between;padding:0 20px 0 23px;font-size:10.5px}
/* about */
.about{left:0;top:954px;width:1200px;height:500px;background:var(--mist)}
.about h2{left:234px;top:52px;font-size:24px}
.about p{left:234px;width:374px;font-size:9.6px;line-height:15px;color:var(--ink)}
/* form */
.estimate{left:0;top:1454px;width:1200px;height:288px;background:var(--navy-form)}
.estimate h2{top:38px;width:100%;text-align:center;color:var(--white);font-size:24px}
.field{width:169px;height:37px;border-radius:19px;background:var(--white);font-size:9.5px;color:#333;display:flex;align-items:center;justify-content:space-between;padding:0 18px}
/* vendors */
.vendors-title{top:1806px;width:100%;text-align:center;font-size:26px}
.vendor-strip{left:228px;top:1860px;width:749px;height:68px;background:#f6f8f3;display:flex;justify-content:space-around;align-items:center}
.vendor-strip span{width:96px;height:34px;border-radius:6px;background:#d9dcd9;display:block}
/* testimonials */
.reviews{left:0;top:1980px;width:1200px;height:346px;background:radial-gradient(circle at 20% 30%,#e6f3fa 0,#cfe8f5 40%,#a9d6ee 100%)}
.reviews h2{top:31px;width:100%;text-align:center;font-size:24px}
.quote-mark{left:335px;top:120px;color:var(--white);font-family:Georgia,serif;font-size:90px;font-weight:700;line-height:1}
.reviews h3{top:125px;width:100%;text-align:center;color:var(--white);font-size:15.5px;font-weight:500}
.reviews p{top:155px;left:405px;width:390px;text-align:center;color:var(--white);font-size:12px;line-height:18px}
.dots{top:226px;left:584px;display:flex;gap:8px}
.dots i{width:6px;height:6px;border-radius:50%;background:var(--navy);display:block}
.dots i.on{background:var(--yellow)}
/* footer */
.footer-text{left:234px;top:2468px;width:244px;font-size:9.5px;line-height:15px;color:var(--muted)}
.col h4{font-size:19px;margin-bottom:14px;color:var(--ink)}
.col li{list-style:none;font-size:9.5px;color:var(--muted);line-height:22.6px}
.subscribe p{font-size:9.5px;line-height:15px;color:var(--muted);width:185px}
.email-box{left:781px;top:2487px;width:183px;height:37px;border:1px solid #c9ccd6;border-radius:19px;font-size:9.5px;color:#333;display:flex;align-items:center;padding-left:16px}
.email-box i{position:absolute;right:3px;top:3px;width:30px;height:30px;border-radius:50%;background:var(--navy);display:block}
.rule{left:234px;top:2597px;width:732px;height:1px;background:var(--line)}
.copy{top:2624px;width:100%;text-align:center;font-size:9.5px;color:var(--muted)}
</style>
</head>
<body>

<!-- top bar -->
<header class="abs topbar">
  <div class="abs social" style="left:234px;top:15px"><span></span><span></span><span></span><span></span></div>
  <div class="abs contact-item" style="left:646px;top:14px">
    <svg width="16" height="12" viewBox="0 0 16 12"><rect x="1" y="1" width="14" height="10" rx="1" fill="none" stroke="#1b2a8c" stroke-width="1.4"/><path d="M1 1l7 6 7-6" fill="none" stroke="#1b2a8c" stroke-width="1.4"/></svg>
    <div><small>If your any query:</small><b>info@tidewellhomecare.example</b></div>
  </div>
  <div class="abs contact-item" style="left:846px;top:14px">
    <svg width="14" height="14" viewBox="0 0 24 24"><path d="M6.6 10.8a15 15 0 006.6 6.6l2.2-2.2a1 1 0 011-.25 11.4 11.4 0 003.6.57 1 1 0 011 1V20a1 1 0 01-1 1A17 17 0 013 4a1 1 0 011-1h3.5a1 1 0 011 1c0 1.25.2 2.45.57 3.57a1 1 0 01-.25 1z" fill="#1b2a8c"/></svg>
    <div><small>Have any question?</small><span class="big">(000) 555 0142</span></div>
  </div>
</header>

<!-- navigation -->
<div class="abs brand" style="left:234px;top:88px"><i></i><span>Tidewell Homecare</span></div>
<nav class="abs nav" style="left:540px;top:104px">
  <a class="on">HOME</a><a>SERVICES</a><a>GIFT CARDS</a><a>ABOUT</a><a>CONTACT</a>
</nav>
<div class="abs btn btn-yellow" style="left:870px;top:89px;width:96px;height:39px">Get A Quote</div>

<!-- hero -->
<section class="abs hero">
  <div class="abs" role="img" aria-label="Photo of a cleaning team in blue uniforms tidying an office" style="left:0;top:0;width:100%;height:100%"></div>
  <div class="abs hero-shade"></div>
  <h1 class="abs script">We Provide High Quality Service</h1>
  <p class="abs">Lorem ipsum dolor sit amet, consectetur adipiscing elit. Aenean condimentum, est at ultricies porta, ipsum ante convallis nisl, ut dictum nulla lacus sit amet ipsum. Pellentesque habitant morbi tristique senectus et netus.</p>
  <svg class="abs" style="left:592px;top:318px" width="16" height="32" viewBox="0 0 16 32"><rect x="1" y="1" width="14" height="24" rx="7" fill="none" stroke="#fff" stroke-width="1.5"/><line x1="8" y1="6" x2="8" y2="11" stroke="#fff" stroke-width="1.5"/><line x1="8" y1="25" x2="8" y2="31" stroke="#fff" stroke-width="1.5"/></svg>
  <svg class="abs" style="left:0;top:330px" width="1200" height="92" viewBox="0 0 1200 92" preserveAspectRatio="none"><path d="M0 92 L0 80 C120 30 300 20 520 46 C760 74 980 40 1200 0 L1200 92 Z" fill="#fff"/></svg>
</section>

<!-- service cards -->
<section>
  <div class="abs card" style="left:234px;background:var(--navy);color:var(--white)">
    <svg class="abs" style="left:158px;top:25px" width="50" height="46" viewBox="0 0 50 46" fill="none" stroke="#fff" stroke-width="2"><path d="M3 20L25 3l22 17"/><path d="M8 17v27h34V17"/><rect x="21" y="31" width="8" height="13"/><rect x="13" y="23" width="6" height="6"/><rect x="31" y="23" width="6" height="6"/><circle cx="25" cy="18" r="3"/></svg>
    <h2 class="script">Residential Cleaning</h2>
    <p>Lorem ipsum dolor sit amet, consectetur adipiscing elit. Aenean condimentum, est at ultricies porta, ipsum ante convallis nisl, ut dictum nulla lacus sit amet ipsum.</p>
    <div class="btn btn-yellow">RESIDENTIAL SERVICES <span>&rarr;</span></div>
  </div>
  <div class="abs card" style="left:600px;background:var(--yellow);color:var(--ink)">
    <svg class="abs" style="left:158px;top:20px" width="50" height="54" viewBox="0 0 50 54" fill="none" stroke="#1d1d2b" stroke-width="2"><rect x="3" y="4" width="26" height="48"/><rect x="22" y="20" width="25" height="32"/><path d="M8 10h5M17 10h5M8 17h5M8 24h5M8 31h5M8 38h5M27 26h4M36 26h4M27 33h4M36 33h4M27 40h4M36 40h4"/><line x1="1" y1="52" x2="49" y2="52"/></svg>
    <h2 class="script">Commercial/Office Cleaning</h2>
    <p>Lorem ipsum dolor sit amet, consectetur adipiscing elit. Aenean condimentum, est at ultricies porta, ipsum ante convallis nisl, ut dictum nulla lacus sit amet ipsum.</p>
    <div class="btn btn-navy">COMMERCIAL SERVICES <span>&rarr;</span></div>
  </div>
  <svg class="abs" style="left:550px;top:615px" width="100" height="92" viewBox="0 0 100 92">
    <path d="M4 0h92l-4 8v72L50 92 8 80V8z" fill="#37b5a3"/>
    <text x="50" y="39" text-anchor="middle" font-family="Poppins,sans-serif" font-weight="700" font-size="13" fill="#fff">THE BEST</text>
    <text x="50" y="51" text-anchor="middle" font-family="Poppins,sans-serif" font-size="8" fill="#fff">Cleaning Service</text>
    <text x="50" y="20" text-anchor="middle" font-size="10" fill="#fff">★ ★ ★</text>
    <text x="50" y="67" text-anchor="middle" font-size="10" fill="#fff">★ ★ ★</text>
  </svg>
</section>

<!-- about -->
<section class="abs about">
  <h2 class="abs script">Hard Work &amp; Reliability</h2>
  <p class="abs" style="top:95px">Lorem ipsum dolor sit amet, consectetur adipiscing elit. Aenean condimentum, est at ultricies porta, ipsum ante convallis nisl, ut dictum nulla lacus sit amet ipsum. Pellentesque habitant morbi tristique senectus et netus et malesuada fames ac turpis egestas. Sed a sapien arcu. Phasellus luctus eros at justo interdum, id luctus nibh fringilla. Nunc ornare felis ut ligula tristique venenatis. Fusce at hendrerit tellus. Vestibulum tempor sit amet velit in fringilla. Sed eget nisi lorem. Proin nisl arcu, pulvinar et purus id, faucibus faucibus augue. Nullam imperdiet velit at vehicula fringilla. Nullam sit amet mattis lacus. Suspendisse placerat odio augue, eu viverra arcu congue sit amet. Aenean nec sagittis dui. Aliquam erat volutpat. Suspendisse vestibulum massa nec maximus condimentum. Sed vulputate tempor nunc quis vestibulum.</p>
  <p class="abs" style="top:274px">Proin tempus aliquet ante, id euismod ligula hendrerit sit amet. Pellentesque lobortis sed neque eget feugiat. Donec eu quam ultricies, mattis ex id, convallis augue. Morbi dapibus tellus turpis, sit amet auctor diam interdum eu. Cras vel suscipit neque. Lorem ipsum dolor sit amet, consectetur adipiscing elit. Nullam faucibus erat non arcu eleifend, eu eleifend diam placerat. Quisque aliquet enim tellus, vel lobortis diam dapibus sed. Sed sollicitudin libero sed sapien porttitor, vel tincidunt nibh fermentum.</p>
  <div class="abs btn btn-yellow" style="left:234px;top:403px;width:158px;height:36px">GET TO KNOW US <span>&rarr;</span></div>
  <div class="abs" role="img" aria-label="Photo of a smiling housekeeper holding a rainbow duster and a basket of cleaning supplies" style="left:653px;top:0;width:547px;height:500px;background:linear-gradient(135deg,#e9e4de 0%,#d7cfc7 40%,#4f6fa8 70%,#c8443f 100%)"></div>
</section>

<!-- estimate form -->
<section class="abs estimate">
  <h2 class="abs script">Free Estimate/Contact Us</h2>
  <div class="abs field" style="left:234px;top:94px">Name*</div>
  <div class="abs field" style="left:422px;top:94px">Email*</div>
  <div class="abs field" style="left:610px;top:94px">City*</div>
  <div class="abs field" style="left:797px;top:94px">Square Footage*</div>
  <div class="abs field" style="left:234px;top:151px">Property Type* <span>&#8964;</span></div>
  <div class="abs field" style="left:422px;top:151px">Type of Cleaning* <span>&#8964;</span></div>
  <div class="abs field" style="left:610px;top:151px">Frequency* <span>&#8964;</span></div>
  <div class="abs field" style="left:797px;top:151px">mm/dd/yy
    <svg width="11" height="11" viewBox="0 0 11 11"><rect x="0.5" y="1.5" width="10" height="9" fill="none" stroke="#1b2a8c"/><rect x="0.5" y="1.5" width="10" height="2.5" fill="#1b2a8c"/></svg>
  </div>
  <div class="abs btn btn-yellow" style="left:546px;top:212px;width:108px;height:36px">SUBMIT <span>&rarr;</span></div>
</section>

<!-- vendors -->
<h2 class="abs script vendors-title">Preferred Vendors</h2>
<div class="abs vendor-strip"><span></span><span></span><span></span><span></span><span></span></div>

<!-- testimonials -->
<section class="abs reviews" role="img" aria-label="Soap bubble background with a squeegee wiping a clean band">
  <h2 class="abs script">What Our Clients Say?</h2>
  <svg class="abs" style="left:258px;top:78px" width="680" height="240" viewBox="0 0 680 240">
    <defs><linearGradient id="panelFill" x1="0" y1="0" x2="0" y2="1"><stop offset="0" stop-color="#5aa9e2"/><stop offset="1" stop-color="#2f7fcc"/></linearGradient></defs>
    <path d="M0 40 C200 -10 460 -8 660 60 L600 238 C420 160 220 170 40 190 C30 130 20 80 0 40 Z" fill="url(#panelFill)"/>
  </svg>
  <div class="abs quote-mark">&ldquo;</div>
  <h3 class="abs">Nora Pell</h3>
  <p class="abs">Lorem ipsum dolor sit amet, consectetur adipiscing elit. Aenean condimentum, est at ultricies porta, ipsum ante convallis nisl, ut dictum nulla lacus sit amet ipsum.</p>
  <div class="abs dots"><i class="on"></i><i></i><i></i></div>
</section>

<!-- footer -->
<footer>
  <div class="abs brand" style="left:234px;top:2400px"><i></i><span>Tidewell Homecare</span></div>
  <p class="abs footer-text">Lorem ipsum dolor sit amet, consectetur adipiscing elit. Duis pulvinar sagittis felis tempus condimentum. In aliquam venenatis dictum.</p>
  <div class="abs social" style="left:234px;top:2532px"><span></span><span></span><span></span><span></span></div>
  <div class="abs col" style="left:524px;top:2410px">
    <h4 class="script">Quick Links</h4>
    <ul><li>Home</li><li>Services</li><li>Gift Cards</li><li>About</li><li>Contact</li></ul>
  </div>
  <div class="abs col" style="left:643px;top:2410px">
    <h4 class="script">Our Services</h4>
    <ul><li>Residential Cleaning</li><li>Commercial Cleaning</li><li>Office Cleaning</li></ul>
  </div>
  <div class="abs col subscribe" style="left:784px;top:2410px">
    <h4 class="script">Subscribe</h4>
    <p>Subscribe to our Newsletter right now to be updated.</p>
  </div>
  <div class="abs email-box">Email Address
    <i><svg width="30" height="30" viewBox="0 0 30 30"><path d="M9 16l12-7-5 13-2-5z" fill="#fff"/></svg></i>
  </div>
  <div class="abs rule"></div>
  <p class="abs copy">Copyright © 2020 Tidewell Homecare . All Rights Reserved.</p>
</footer>

</body>
</html>
```